依頼詳細
作成している原稿があるので別途添付いたします。
記載項目
作成原稿にすべて入れています。
サイズ
A4
ページ数
片面
希望イメージ
シンプル 複雑
単色 カラフル
暗い 明るい
日常 高級
遊び心 厳粛
未来的 伝統的
女性的 男性的
希望する色
無彩色系、無彩色系ですが明るめの色もあれば見たいです
納品ファイル
• イラストレーター形式 (.ai)
• PNG形式 (.png)
補足説明

```html
<!DOCTYPE html>
<html lang="ja">
<head>
<meta charset="utf-8">
<title>ご縁結び塾 群馬校 開講プレ講演会</title>
<link href="https://fonts.googleapis.com/css2?family=Noto+Sans+JP:wght@400;700;900&family=Noto+Serif+JP:wght@700;900&display=swap" rel="stylesheet">
<style>
  :root {
    --ink: #1a1a1a;
    --red: #d7141e;
    --paper: #ffffff;
    --grey: #6b6b6b;
    --line: #9a9a9a;
    --photo-a: #f2f1ef;
    --photo-b: #b9b4ad;
    --tint: #f4f4f4;
  }
  * { margin: 0; padding: 0; box-sizing: border-box; }
  html, body { width: 849px; height: 1200px; overflow: hidden; background: var(--paper); }
  body { font-family: "Noto Sans JP", sans-serif; color: var(--ink); }
  .poster { position: relative; width: 849px; height: 1200px; overflow: hidden; background: var(--paper); }

  .speaker-photo {
    position: absolute; left: 430px; top: 40px; width: 419px; height: 530px;
    background: radial-gradient(ellipse at 55% 40%, var(--photo-a) 0%, #d8d4ce 55%, var(--photo-b) 100%);
  }

  .event-label { position: absolute; left: 88px; top: 10px; }
  .event-label .roman { font-size: 9px; letter-spacing: 3px; color: var(--grey); text-align: center; }
  .event-label .title { font-size: 17px; font-weight: 700; letter-spacing: 1px; }

  .headline {
    position: absolute; left: 34px; top: 44px;
    font-family: "Noto Serif JP", serif; font-weight: 900; line-height: 1.04;
    font-size: 84px; letter-spacing: -2px;
  }
  .headline .line { display: block; white-space: nowrap; }
  .headline .accent { color: var(--red); }
  .headline .big { font-size: 112px; }
  .headline .l3 { margin-top: 4px; }
  .headline .l4 { padding-left: 210px; }

  .speaker-name { position: absolute; left: 36px; top: 548px; display: flex; align-items: baseline; gap: 16px; }
  .speaker-name .ja { font-family: "Noto Serif JP", serif; font-weight: 900; font-size: 40px; letter-spacing: 4px; }
  .speaker-name .ja small { font-size: 22px; letter-spacing: 0; }
  .speaker-name .en { font-style: italic; font-size: 16px; color: var(--grey); }

  .rules { position: absolute; left: 30px; top: 624px; width: 370px; border: 2px solid var(--ink); padding: 8px 16px 10px; background: var(--paper); }
  .rules .lead { font-size: 13px; font-weight: 700; color: var(--red); text-align: center; line-height: 1.5; }
  .rules .title { font-size: 22px; font-weight: 900; text-align: center; background: var(--tint); margin: 4px 0 6px; line-height: 1.4; }
  .rules ol { list-style: none; font-size: 12.5px; font-weight: 700; line-height: 1.55; }

  .when-where { position: absolute; left: 420px; top: 640px; width: 410px; }
  .when-where .date { font-family: "Noto Serif JP", serif; font-weight: 900; color: var(--red); font-size: 42px; letter-spacing: -1px; line-height: 1.3; }
  .when-where .date .dow { display: inline-block; width: 36px; height: 36px; line-height: 36px; text-align: center; background: var(--red); color: var(--paper); font-size: 22px; border-radius: 4px; vertical-align: 6px; }
  .when-where .venue { font-family: "Noto Serif JP", serif; font-weight: 900; font-size: 38px; letter-spacing: -1px; margin-top: 2px; line-height: 1.3; }
  .when-where .detail { font-size: 10px; margin-top: 6px; }

  .schedule { position: absolute; left: 30px; top: 808px; width: 789px; }
  .schedule .head { display: flex; align-items: center; gap: 12px; border-bottom: 2px solid var(--ink); padding-bottom: 4px; }
  .schedule .head h2 { font-size: 18px; font-weight: 900; }
  .schedule .head .badge { background: var(--red); color: var(--paper); font-size: 13px; font-weight: 700; padding: 2px 10px; }
  .schedule .head .note { margin-left: auto; font-size: 10px; }
  .schedule .cols { display: flex; gap: 20px; margin-top: 8px; }
  .schedule table { flex: 1; border-collapse: collapse; font-size: 11.5px; }
  .schedule td { border-bottom: 1px solid var(--line); padding: 8px 4px; }
  .schedule td.no { background: var(--ink); color: var(--paper); font-weight: 700; width: 52px; text-align: center; }
  .schedule td.theme { font-weight: 700; }
  .schedule td.day { font-size: 10px; white-space: nowrap; }

  .tickets { position: absolute; left: 30px; top: 985px; width: 789px; height: 150px; border: 1.5px solid var(--ink); display: flex; font-size: 10.5px; }
  .tickets .col { padding: 10px 12px; border-right: 1px solid var(--line); flex: 1; line-height: 1.6; }
  .tickets .col:last-child { border-right: none; }
  .tickets .tag { display: inline-block; background: var(--ink); color: var(--paper); font-weight: 700; padding: 0 8px; margin-bottom: 4px; }

  .organizer { position: absolute; left: 0; right: 0; top: 1155px; text-align: center; font-size: 16px; font-weight: 700; }
</style>
</head>
<body>
<div class="poster">
  <div class="speaker-photo" role="img" aria-label="マイクを手に語る講師の写真"></div>

  <div class="event-label">
    <p class="roman">GO-EN MUSUBI</p>
    <p class="title">ご縁結び塾 群馬校　開講プレ講演会</p>
  </div>

  <h1 class="headline">
    <span class="line">出会いこそ</span>
    <span class="line"><span class="accent big">宝</span>である</span>
    <span class="line l3">人のご縁で</span>
    <span class="line l4 accent">でっかく</span>
    <span class="line">生きろ!</span>
  </h1>

  <div class="speaker-name">
    <span class="ja">中山 文彦<small>氏</small></span>
    <span class="en">Fumihiko Nakayama</span>
  </div>

  <section class="rules">
    <p class="lead">今日あなたの心にスイッチが入ります</p>
    <p class="title">「4つの鉄板ルール」</p>
    <ol>
      <li>1. 返事は0.2秒!</li>
      <li>2. 頼まれごとは試されごと!</li>
      <li>3. 出来ない理由を言わない!</li>
      <li>4. そのうち・と言わずやることをやる!</li>
    </ol>
  </section>

  <section class="when-where">
    <p class="date">2020年7月11日<span class="dow">土</span></p>
    <p class="venue">高原シティホール</p>
    <p class="detail">開場 18時30分〜 ／ 開演 19時 ｜ 群馬県高原市松風町12-3　TEL.000-000-0000</p>
  </section>

  <section class="schedule">
    <div class="head">
      <h2>ご縁結び塾 群馬校 1期 開催予定</h2>
      <span class="badge">受講生募集中</span>
      <span class="note">時間：各回19時〜21時</span>
    </div>
    <div class="cols">
      <table>
        <tr><td class="no">第1講義</td><td class="theme">「人に出会って心に出会う」</td><td class="day">9月6日(日)</td></tr>
        <tr><td class="no">第2講義</td><td class="theme">「まくぼ1年に、というところ」</td><td class="day">10月4日(日)</td></tr>
        <tr><td class="no">第3講義</td><td class="theme">「言葉の力」</td><td class="day">11月1日(日)</td></tr>
      </table>
      <table>
        <tr><td class="no">第4講義</td><td class="theme">「足るを知る」</td><td class="day">12月6日(日)</td></tr>
        <tr><td class="no">第5講義</td><td class="theme">「プロデュースする」</td><td class="day">1月10日(日)</td></tr>
        <tr><td class="no">第6講義</td><td class="theme">「自分の役割を発見」</td><td class="day">2月7日(日)</td></tr>
      </table>
    </div>
  </section>

  <section class="tickets">
    <div class="col">
      <span class="tag">チケット</span><br>
      一般 3,000円（当日3,500円）<br>学生 1,500円<br>全席自由・先着順となります
    </div>
    <div class="col">
      <span class="tag">お申し込み</span><br>
      専用フォームまたはお電話にて<br>お名前・人数をお知らせください<br>受付は7月10日まで
    </div>
    <div class="col">
      <span class="tag">お問い合わせ</span><br>
      ご縁結び実行委員会 事務局<br>TEL.000-000-0000<br>平日10時〜17時
    </div>
  </section>

  <p class="organizer">主催：ご縁結び実行委員会</p>
</div>
</body>
</html>
```